A3 Event Poster for School Fundraiser

We are looking for a bold, engaging, and professional A3 poster design to promote a special school fundraising event. A top athlete will be visiting a primary school to inspire children, encourage participation in sport, and help launch a fundraising initiative to raise money for new PE/sports equipment for the school.

The poster will be displayed prominently outside the school and shared with parents and families. Its purpose is to generate excitement, explain the event quickly, and encourage parents/families to sponsor and get involved.

We work with about 50 different athletes so will need the design to be easy to alter the picture of the athlete/name etc so it can be replicated across the different athletes.

Target Market(s)

Priamary School Parents/Communities

Industry/Entity Type

Education

Font styles to use
Other font styles liked:
• The logo font is Rajdhani. ‘Corvel’ is bold, ‘Pennix’ is semibold and the strapline is regular.

Requirements
Must have
• Space for the Event Date (that school can write in themselves), A picture of the visiting athlete and their bio (with ability to easily change)
Nice to have
• Bold, eye-catching

```html
<!DOCTYPE html>
<html lang="en">
<head>
<meta charset="utf-8">
<title>Corvel Pennix – Inspirational Athlete Visit</title>
<link href="https://fonts.googleapis.com/css2?family=Rajdhani:wght@400;500;600;700&family=Roboto:wght@400;500;700&family=Roboto+Condensed:wght@700&family=Poppins:wght@400;500;600;700&display=swap" rel="stylesheet">
<style>
  :root{
    --purple:#6a2b82;
    --red:#e01e36;
    --blue:#0b3ca6;
    --blue-deep:#07329a;
    --cyan:#2bd0f0;
    --navy:#1d3b9a;
    --ink:#1c1c1c;
    --white:#ffffff;
    --stage:#e9e9ea;
    --rule:#b9c4dc;
  }
  *{box-sizing:border-box;margin:0;padding:0}
  html,body{width:906px;height:1200px;overflow:hidden;background:var(--stage)}
  .poster{position:absolute;left:42px;top:20px;width:821px;height:1160px;background:var(--white);overflow:hidden;font-family:'Poppins',sans-serif}
  .abs{position:absolute}

  .brand{left:252px;top:62px;display:flex;align-items:center;gap:8px}
  .brand__dot{width:30px;height:30px;border-radius:50%;background:var(--red)}
  .brand__name{font-family:'Rajdhani',sans-serif;font-weight:600;font-size:44px;line-height:1;color:var(--purple)}
  .brand__tag{left:298px;top:106px;font-family:'Rajdhani',sans-serif;font-weight:400;font-size:13px;color:var(--purple)}

  .ribbon{left:258px;top:147px;width:304px;height:52px;background:var(--red);
    clip-path:polygon(0 0,100% 0,96% 50%,100% 100%,0 100%,4% 50%);
    color:var(--white);font-family:'Rajdhani',sans-serif;font-weight:500;font-size:38px;letter-spacing:1px;
    display:flex;align-items:center;justify-content:center;padding-top:3px}
  .cheer{top:143px;width:66px;height:64px;background:var(--purple);border-radius:50% 50% 8px 8px;opacity:.9}
  .cheer--left{left:174px}
  .cheer--right{left:581px}

  .headline{left:0;width:821px;top:222px;text-align:center;font-family:'Poppins',sans-serif;font-weight:700;font-size:150px;line-height:1.05;letter-spacing:-3px;color:var(--purple)}
  .subhead{left:0;width:821px;top:354px;text-align:center;font-family:'Roboto',sans-serif;font-weight:400;font-size:58px;line-height:1;color:var(--ink)}

  .info{left:0;top:451px;width:440px;height:365px;
    background:radial-gradient(circle at 70% 10%,#1a55c8 0%,var(--blue) 45%,var(--blue-deep) 100%)}
  .badge{left:66px;top:478px;width:139px;height:72px;background:var(--white);border-radius:9px}
  .role{left:219px;top:494px;font-family:'Rajdhani',sans-serif;font-weight:700;font-size:26px;line-height:1.25;color:var(--white)}
  .athlete-name{left:64px;top:560px;font-family:'Roboto',sans-serif;font-weight:500;font-size:54px;line-height:1;color:var(--cyan)}
  .name-rule{left:181px;top:602px;width:207px;height:1px;background:var(--rule)}
  .bio{left:65px;top:618px;width:340px;font-size:16.3px;line-height:20px;color:var(--white)}
  .bio-rule{left:65px;top:716px;width:322px;height:1px;background:var(--rule)}
  .date-label{left:65px;top:731px;font-family:'Rajdhani',sans-serif;font-weight:700;font-size:26px;color:var(--white)}
  .date-value{left:65px;top:759px;font-family:'Roboto',sans-serif;font-weight:700;font-size:37px;color:var(--cyan)}

  .appeal{left:0;top:821px;width:480px;height:101px;background:var(--red)}
  .appeal__icon{left:56px;top:838px}
  .appeal__lead{left:152px;top:842px;font-family:'Roboto',sans-serif;font-weight:500;font-size:19px;color:var(--white)}
  .appeal__focus{left:152px;top:864px;font-family:'Roboto Condensed',sans-serif;font-weight:700;font-size:32px;color:var(--cyan)}

  .portrait{left:440px;top:445px;width:317px;height:482px;border:8px solid var(--white);
    border-radius:34px 34px 34px 60px;
    background:linear-gradient(160deg,#dfe6f2 0%,#2d55b0 45%,#1c2240 75%,#c7d2ea 100%)}

  .pillars{left:0;top:952px;width:821px;height:70px}
  .pillar{position:absolute;display:flex;align-items:center;gap:8px}
  .pillar__badge{width:70px;height:70px;border-radius:50%;border:5px solid var(--cyan);background:var(--navy);
    box-shadow:inset 0 0 0 3px var(--white);display:flex;align-items:center;justify-content:center}
  .pillar__text{font-weight:600;font-size:24.5px;line-height:1.1;color:var(--ink)}
  .pillar--inspire{left:70px}
  .pillar--difference{left:323px}
  .pillar--active{left:600px}
  .pillar-divider{position:absolute;top:3px;width:1px;height:62px;background:#c9c9c9}

  .mission{left:67px;top:1046px;width:686px;height:45px;border-radius:23px;background:var(--red);
    color:var(--white);font-weight:700;font-size:20.5px;display:flex;align-items:center;justify-content:center}
</style>
</head>
<body>
<main class="poster">
  <div class="brand abs"><span class="brand__dot"></span><span class="brand__name">CorvelPennix</span></div>
  <div class="brand__tag abs">Inspiring every child</div>

  <div class="cheer cheer--left abs" role="img" aria-label="Cheering figure"></div>
  <div class="ribbon abs">INSPIRATIONAL</div>
  <div class="cheer cheer--right abs" role="img" aria-label="Cheering figure"></div>

  <h1 class="headline abs">ATHLETE</h1>
  <p class="subhead abs">Visiting our school</p>

  <section class="info abs"></section>
  <div class="badge abs"></div>
  <p class="role abs">Olympic<br>Volleyball Player</p>
  <h2 class="athlete-name abs">Darren</h2>
  <div class="name-rule abs"></div>
  <p class="bio abs">Is a dynamic English volleyball player &amp; coach, known for his leadership on &amp; off the court &amp; his passion for inspiring the next generation through sport.</p>
  <div class="bio-rule abs"></div>
  <p class="date-label abs">Event Date</p>
  <p class="date-value abs">Saturday, 20th June</p>

  <section class="appeal abs"></section>
  <svg class="appeal__icon abs" width="86" height="64" viewBox="0 0 86 64" aria-hidden="true">
    <path d="M8 26 L48 10 L48 52 L8 38 Z" fill="#ffffff"/>
    <rect x="2" y="24" width="10" height="16" rx="3" fill="#1d3b9a"/>
    <ellipse cx="48" cy="31" rx="7" ry="21" fill="#1d3b9a"/>
    <path d="M16 38 L22 56 L30 56 L26 40 Z" fill="#1d3b9a"/>
    <path d="M62 18 L72 12 L70 20 L80 6" stroke="#1d3b9a" stroke-width="3" fill="none"/>
    <path d="M62 44 L72 50 L70 42 L80 58" stroke="#1d3b9a" stroke-width="3" fill="none"/>
  </svg>
  <p class="appeal__lead abs">Help us raise funds for new</p>
  <p class="appeal__focus abs">Sports Equipment</p>

  <div class="portrait abs" role="img" aria-label="Photo of the visiting athlete in team jacket"></div>

  <section class="pillars abs">
    <div class="pillar pillar--inspire">
      <span class="pillar__badge">
        <svg width="34" height="34" viewBox="0 0 34 34" aria-hidden="true">
          <circle cx="19" cy="10" r="5" fill="#fff"/><rect x="17" y="15" width="4" height="4" fill="#fff"/>
          <path d="M3 22 h5 v9 h-5z M9 24 h8 q4 0 6 -2 l6 -3 q2 2 0 4 l-9 6 h-11z" fill="#fff"/>
        </svg>
      </span>
      <span class="pillar__text">Be<br>inspired</span>
    </div>
    <span class="pillar-divider" style="left:282px"></span>
    <div class="pillar pillar--difference">
      <span class="pillar__badge">
        <svg width="34" height="34" viewBox="0 0 34 34" aria-hidden="true">
          <circle cx="17" cy="7" r="4" fill="#fff"/>
          <path d="M13 13 h8 v9 h-2 v10 h-4 v-10 h-2z M6 8 l7 6 M28 8 l-7 6" stroke="#fff" stroke-width="2.5" fill="#fff"/>
        </svg>
      </span>
      <span class="pillar__text">Make a<br>difference</span>
    </div>
    <span class="pillar-divider" style="left:559px"></span>
    <div class="pillar pillar--active">
      <span class="pillar__badge">
        <svg width="34" height="34" viewBox="0 0 34 34" aria-hidden="true">
          <circle cx="10" cy="12" r="3.5" fill="#fff"/><circle cx="23" cy="8" r="3.5" fill="#fff"/>
          <path d="M6 17 h8 l2 8 h-3 v6 h-4 v-6 h-3z M20 13 h7 l3 9 h-3 l-1 9 h-4 l-1 -9 h-3z" fill="#fff"/>
        </svg>
      </span>
      <span class="pillar__text">Get<br>Active</span>
    </div>
  </section>

  <p class="mission abs">Inspiring every child to lead an active, resilient &amp; healthy life</p>
</main>
</body>
</html>
```